Mortgage Service Company Mail Offer - TRI-FOLD (8.5"x11" Sides) format

Dear designer,

As we really appreciate the logo we received on PlanoForge, we decided to use your service for our bi-fold marketing brochure.

Our company is a private alternative offering mortgage financing to individuals and businesses who do not fulfill conventional financial institutions conditions, or who need money quickly.

I have attached our current homemade brochure which is a 8.5x11 standard sheet which is really basic. We would like to have the same information on a TRI-FOLD format. We will need a French and a English version of the brochure.

*Must Have Priorities
Colour - Blue as our logo and Orange OR Blue as our logo and Green
Logo - Our logo needs to be on the brochure
Picture - A black male need to be in one of the pictures.
Business card - It needs to have one place in the brochure where I can glue a business card; probably on the back of the brochure.
Testimonial - Our current brochure only has 1 testimonial but we would like room for 3.

*Nice to Have Priorities
Picture - Couple and home
Picture - In addition to the black male, one of the picture will need to have an asian, a ispanic OR a indonesian male or female.
Picture - People that calculate (e.g. slide 3 of the slider here http://www.kelbrooklending.ca./index.php)
Design - It need to be clear that the brochure is the reach individual who received a 60-day notice from their financial institution.

*Should not have
It should not be a simple cut & past of our current brochure in a bi-fold format.

Target Market(s)

People in financial distress.

Industry/Entity Type

Marketing

Requirements
Must have
• Colour - Blue as our logo and Orange OR Blue as our logo and Green
Nice to have
• Picture - Couple and home
Should not have
• It should not be a simple cut & past of our current brochure in a bi-fold format.

```html
<!DOCTYPE html>
<html lang="en">
<head>
<meta charset="utf-8">
<title>Halden Financial – Tri-fold Brochure</title>
<link rel="stylesheet" href="https://fonts.googleapis.com/css2?family=Arimo:wght@700&family=Cinzel:wght@600&family=Didact+Gothic&family=Oswald:wght@500&family=PT+Sans:ital@1&family=Raleway:wght@600&display=swap">
<style>
  :root{
    --navy:#1d2f63;
    --blue:#1f86bd;
    --orange:#f06a24;
    --amber:#f8b21c;
    --text:#3c3c3c;
    --paper:#fafafa;
    --fold:#d9d9d9;
    --bg:#e9e7e4;
  }
  *{margin:0;padding:0;box-sizing:border-box}
  html,body{width:1200px;height:954px;overflow:hidden;background:var(--bg)}
  .brochure{position:absolute;left:20px;top:28px;width:1160px;height:897px;background:var(--paper);box-shadow:0 2px 8px rgba(0,0,0,.18);overflow:hidden}
  .panel{position:absolute;top:0;width:387px;height:897px;background:linear-gradient(180deg,#fff 0%,#f3f3f3 100%)}
  .panel--left{left:0}
  .panel--middle{left:387px;border-left:1px solid var(--fold)}
  .panel--right{left:773px;border-left:1px solid var(--fold)}
  .band{position:absolute;left:0;bottom:0;width:100%;height:17px}
  .band--orange{background:linear-gradient(90deg,var(--orange) 0%,var(--amber) 50%,var(--orange) 100%)}
  .band--blue{background:linear-gradient(90deg,var(--navy) 0%,var(--blue) 50%,var(--navy) 100%)}
  .photo{position:absolute}
  .photo--meeting{left:0;top:0;width:387px;height:265px;background:linear-gradient(135deg,#eef1f4 0%,#c9ced6 45%,#2b3552 100%);clip-path:polygon(0 0,100% 0,100% 72%,86% 100%,0 100%)}
  .corner-accent{position:absolute;left:0;top:0;width:0;height:0;border-top:44px solid var(--orange);border-right:70px solid transparent}
  .photo--house{left:0;top:259px;width:387px;height:348px;background:linear-gradient(180deg,#e6e6e4 0%,#b7aca3 35%,#8e857c 55%,#5f8a3a 72%,#3f7a25 100%)}
  .photo--couple{left:0;top:227px;width:387px;height:380px;background:linear-gradient(160deg,#8fb2d6 0%,#d9e4ee 35%,#d9b48a 60%,#6f7d5a 100%);clip-path:polygon(0 0,100% 0,100% 79%,93% 100%,0 100%)}
  .heading-testimonials{position:absolute;left:35px;top:294px;font-family:'Cinzel',serif;font-weight:600;font-size:23px;color:var(--navy);letter-spacing:.5px;padding-bottom:2px;border-bottom:2px solid var(--orange)}
  .testimonial{position:absolute;left:34px;width:314px}
  .testimonial__text{font-family:'Didact Gothic',sans-serif;font-size:12.6px;line-height:15.7px;color:var(--text);text-align:justify;text-indent:46px;position:relative}
  .quote{position:absolute;width:40px;height:26px}
  .quote--open{left:0;top:-3px}
  .quote--close{right:0;bottom:-22px}
  .testimonial__author{position:absolute;right:0;font-family:'PT Sans',sans-serif;font-style:italic;font-size:13.5px;color:var(--navy)}
  .tollfree{position:absolute;font-family:'Arimo',sans-serif;font-weight:700;color:var(--navy);display:flex;align-items:center;gap:4px}
  .tollfree--footer{left:67px;top:852px;font-size:20px}
  .tollfree--ribbon{left:70px;top:197px;font-size:19px;color:#fff}
  .ribbon{position:absolute;left:0;top:157px;width:365px;height:102px}
  .brand{position:absolute;display:flex;align-items:center;gap:10px;font-family:'Raleway',sans-serif;font-weight:600;color:var(--navy);letter-spacing:1px}
  .brand__mark{background:var(--navy)}
  .brand--top{left:44px;top:92px;font-size:30px}
  .brand--top .brand__mark{width:22px;height:22px}
  .brand--contact{left:80px;top:664px;font-size:23px}
  .brand--contact .brand__mark{width:16px;height:16px}
  .contact{position:absolute;left:76px;font-family:'Didact Gothic',sans-serif;font-size:12.8px;line-height:17px;color:var(--text)}
  .contact__icon{position:absolute;left:-20px;top:2px;width:12px;height:12px}
  .headline{position:absolute;left:0;width:387px;top:682px;text-align:center;font-family:'Oswald',sans-serif;font-weight:500;font-size:33px;line-height:41px;color:var(--orange)}
  .web{position:absolute;left:57px;top:853px;font-family:'Arimo',sans-serif;font-size:19px;color:var(--navy);display:flex;align-items:center;gap:6px;font-weight:400}
</style>
</head>
<body>
<main class="brochure">

  <section class="panel panel--left">
    <div class="photo photo--meeting" role="img" aria-label="Photo: advisor shaking hands with a smiling couple across a desk"></div>
    <div class="corner-accent"></div>

    <h2 class="heading-testimonials">Testimonials</h2>

    <blockquote class="testimonial" style="top:344px">
      <svg class="quote quote--open" viewBox="0 0 40 26"><path d="M2 26V12C2 4 7 1 14 0v6c-3 1-5 3-5 6h5v14zM22 26V12c0-8 5-11 12-12v6c-3 1-5 3-5 6h5v14z" fill="#d3d3d3"/></svg>
      <p class="testimonial__text">Lorem ipsum dolor sit amet, consectetuer adipiscing elit, sed diam nonummy nibh euismod tincidunt ut laoreet dolore magna aliquam erat volutpat. Ut wisi enim ad minim veniam, quis nostrud exerci tation ullamcorper suscipit lobortis nisl ut aliquip ex ea commodo consequat.</p>
      <svg class="quote quote--close" viewBox="0 0 40 26"><path d="M38 0v14c0 8-5 11-12 12v-6c3-1 5-3 5-6h-5V0zM18 0v14c0 8-5 11-12 12v-6c3-1 5-3 5-6H6V0z" fill="#d3d3d3"/></svg>
      <cite class="testimonial__author" style="top:126px">— Abcdef Ghijklmnopqrst</cite>
    </blockquote>

    <blockquote class="testimonial" style="top:505px">
      <svg class="quote quote--open" viewBox="0 0 40 26"><path d="M2 26V12C2 4 7 1 14 0v6c-3 1-5 3-5 6h5v14zM22 26V12c0-8 5-11 12-12v6c-3 1-5 3-5 6h5v14z" fill="#d3d3d3"/></svg>
      <p class="testimonial__text">Lorem ipsum dolor sit amet, consectetuer adipiscing elit, sed diam nonummy nibh euismod tincidunt ut laoreet dolore magna aliquam erat volutpat. Ut wisi enim ad minim veniam, quis nostrud exerci tation ullamcorper suscipit lobortis nisl ut aliquip ex ea commodo consequat.</p>
      <svg class="quote quote--close" viewBox="0 0 40 26"><path d="M38 0v14c0 8-5 11-12 12v-6c3-1 5-3 5-6h-5V0zM18 0v14c0 8-5 11-12 12v-6c3-1 5-3 5-6H6V0z" fill="#d3d3d3"/></svg>
      <cite class="testimonial__author" style="top:127px">— Abcdef Ghijklmnopqrst</cite>
    </blockquote>

    <blockquote class="testimonial" style="top:671px">
      <svg class="quote quote--open" viewBox="0 0 40 26"><path d="M2 26V12C2 4 7 1 14 0v6c-3 1-5 3-5 6h5v14zM22 26V12c0-8 5-11 12-12v6c-3 1-5 3-5 6h5v14z" fill="#d3d3d3"/></svg>
      <p class="testimonial__text">Lorem ipsum dolor sit amet, consectetuer adipiscing elit, sed diam nonummy nibh euismod tincidunt ut laoreet dolore magna aliquam erat volutpat. Ut wisi enim ad minim veniam, quis nostrud exerci tation ullamcorper suscipit lobortis nisl ut aliquip ex ea commodo consequat.</p>
      <svg class="quote quote--close" viewBox="0 0 40 26"><path d="M38 0v14c0 8-5 11-12 12v-6c3-1 5-3 5-6h-5V0zM18 0v14c0 8-5 11-12 12v-6c3-1 5-3 5-6H6V0z" fill="#d3d3d3"/></svg>
      <cite class="testimonial__author" style="top:127px">— Abcdef Ghijklmnopqrst</cite>
    </blockquote>

    <p class="tollfree tollfree--footer">Toll-Free
      <svg width="20" height="20" viewBox="0 0 20 20"><circle cx="10" cy="10" r="9" fill="none" stroke="#f06a24" stroke-width="1.6"/><path d="M7 5.5c-1.5 1.5-1 4.5 1.5 7s5 3 6 2l-1.5-2-1.5.8c-1-.5-2.5-2-3-3l.8-1.5z" fill="#f06a24"/></svg>
      (877) 418-5526</p>
    <div class="band band--orange"></div>
  </section>

  <section class="panel panel--middle">
    <div class="photo photo--house" role="img" aria-label="Photo: brick family house with a green front lawn"></div>
    <svg class="ribbon" viewBox="0 0 365 102">
      <defs><linearGradient id="ribbonFill" x1="0" x2="1"><stop offset="0" stop-color="#1d2f63"/><stop offset=".55" stop-color="#1d4f86"/><stop offset="1" stop-color="#1f86bd"/></linearGradient></defs>
      <polygon points="0,78 100,0 365,0 365,102 0,102" fill="url(#ribbonFill)"/>
      <polygon points="365,0 386,30 365,30" fill="#111"/>
    </svg>
    <p class="tollfree tollfree--ribbon">Toll-Free
      <svg width="20" height="20" viewBox="0 0 20 20"><circle cx="10" cy="10" r="9" fill="none" stroke="#f06a24" stroke-width="1.6"/><path d="M7 5.5c-1.5 1.5-1 4.5 1.5 7s5 3 6 2l-1.5-2-1.5.8c-1-.5-2.5-2-3-3l.8-1.5z" fill="#f06a24"/></svg>
      (877) 418-5526</p>

    <div class="brand brand--contact"><span class="brand__mark"></span>HALDEN FINANCIAL</div>

    <p class="contact" style="top:727px">
      <svg class="contact__icon" viewBox="0 0 12 12"><path d="M6 0a4 4 0 0 0-4 4c0 3 4 8 4 8s4-5 4-8a4 4 0 0 0-4-4zm0 5.5A1.5 1.5 0 1 1 6 2.5a1.5 1.5 0 0 1 0 3z" fill="#f06a24"/></svg>
      2140, rue Belcourt Est, Suite 310<br>Montréal (Québec) H2X 9Z9</p>
    <p class="contact" style="top:779px">
      <svg class="contact__icon" viewBox="0 0 12 12"><path d="M1 4c0-2 10-2 10 0v1H8V4H4v1H1zM3 6h6l1 5H2z" fill="#f06a24"/></svg>
      1 (877) 418-5526</p>
    <p class="contact" style="top:796px">
      <svg class="contact__icon" viewBox="0 0 12 12"><path d="M3 1h5v3H3zM1 5h10v5H9v-2H3v2H1zM3 9h6v3H3z" fill="none" stroke="#f06a24" stroke-width="1"/></svg>
      1 (877) 418-5590</p>
    <p class="contact" style="top:831px">
      <svg class="contact__icon" viewBox="0 0 12 12"><rect x=".5" y="2" width="11" height="8" fill="none" stroke="#f06a24"/><path d="M.5 2l5.5 4.5L11.5 2" fill="none" stroke="#f06a24"/></svg>
      info@haldenfinancial.ca</p>
    <p class="contact" style="top:848px">
      <svg class="contact__icon" viewBox="0 0 12 12"><circle cx="6" cy="6" r="5.3" fill="none" stroke="#f06a24"/><path d="M.7 6h10.6M6 .7c-3 3-3 7.6 0 10.6M6 .7c3 3 3 7.6 0 10.6" fill="none" stroke="#f06a24" stroke-width=".8"/></svg>
      www.haldenfinancial.ca</p>
    <div class="band band--blue"></div>
  </section>

  <section class="panel panel--right">
    <div class="brand brand--top"><span class="brand__mark"></span>HALDEN FINANCIAL</div>
    <div class="photo photo--couple" role="img" aria-label="Photo: happy couple outdoors under a blue sky"></div>
    <h1 class="headline">WE ARE THE SOLUTION<br>TO A 60-DAY NOTICE!</h1>
    <p class="web">
      <svg width="21" height="21" viewBox="0 0 12 12"><circle cx="6" cy="6" r="5.3" fill="none" stroke="#f06a24" stroke-width=".8"/><path d="M.7 6h10.6M6 .7c-3 3-3 7.6 0 10.6M6 .7c3 3 3 7.6 0 10.6M1.5 3.3h9M1.5 8.7h9" fill="none" stroke="#f06a24" stroke-width=".6"/></svg>
      www.haldenfinancial.ca</p>
    <div class="band band--orange"></div>
  </section>

</main>
</body>
</html>
```